We are looking to recreate our Harmon & Company Jobsite Sign. This sign will be placed by the street at each of our jobsites. We want to keep this sign simple, but at the same time, want to add a catching appeal to the design for anyone passing by. We want to stick to a two color scheme (Harmon Blue, and White). Please only use the Company Logo that I have uploaded for this project. Please also see a mock up of what we would like to include on this sign. The Sign Dimensions will be 4' x 8'. Please keep all verbiage uniform with the verbiage on the sample design I have uploaded. LET YOUR CREATIVITY FLOW!

```html
<!DOCTYPE html>
<html lang="en">
<head>
<meta charset="utf-8">
<title>Harmon &amp; Company Jobsite Sign</title>
<link href="https://fonts.googleapis.com/css2?family=Crimson+Pro:wght@400;600;700&display=swap" rel="stylesheet">
<style>
  :root {
    --harmon-blue: #353d92;
    --harmon-blue-deep: #262c78;
    --harmon-blue-light: #5a63b0;
    --navy-text: #232a78;
    --sign-white: #eef0f5;
    --stripe-gray: #a9acb3;
    --band-charcoal: #45484f;
    --band-gray: #75787f;
    --page-bg: #b4bccb;
  }
  * { margin: 0; padding: 0; box-sizing: border-box; }
  html, body {
    width: 1200px; height: 900px; overflow: hidden;
    background: var(--page-bg);
    font-family: "Crimson Pro", serif;
  }
  .sign {
    position: absolute; left: 40px; top: 170px;
    width: 1120px; height: 560px;
    background: var(--sign-white);
    overflow: hidden;
  }
  .sign-shapes { position: absolute; inset: 0; }
  .brand {
    position: absolute; left: 200px; top: 34px;
    color: var(--navy-text); font-weight: 600;
  }
  .brand-name { font-size: 76px; line-height: 0.9; display: block; }
  .brand-sub { font-size: 32px; line-height: 1.1; display: block; padding-left: 4px; }
  .brand-divider {
    position: absolute; left: 520px; top: 34px;
    width: 3px; height: 104px; background: var(--navy-text);
  }
  .trade {
    position: absolute; left: 546px; top: 30px;
    color: var(--navy-text); font-weight: 600;
    font-size: 46px; line-height: 1.05; letter-spacing: 4px;
  }
  .trade span { display: block; }
  .trade .first { padding-left: 50px; }
  .headline {
    position: absolute; left: 200px; right: 0; top: 190px;
    text-align: center; color: var(--sign-white);
    font-weight: 600; font-size: 92px; line-height: 0.98;
  }
  .details {
    position: absolute; left: 280px; right: 40px; top: 414px;
    display: flex; align-items: center; gap: 56px;
    color: var(--sign-white); font-size: 24px;
  }
  .social { display: flex; gap: 22px; }
  .social-square { width: 22px; height: 22px; background: var(--sign-white); }
  .location { font-size: 26px; }
  .phone {
    position: absolute; left: 30px; top: 474px;
    color: var(--sign-white); font-size: 56px; font-weight: 400;
  }
  .website {
    position: absolute; right: 50px; top: 482px;
    color: var(--navy-text); font-size: 46px; font-weight: 700;
  }
</style>
</head>
<body>
  <div class="sign">
    <svg class="sign-shapes" width="1120" height="560" viewBox="0 0 1120 560">
      <defs>
        <linearGradient id="blueBand" x1="0" y1="0" x2="1" y2="1">
          <stop offset="0" stop-color="var(--harmon-blue-light)"/>
          <stop offset="0.45" stop-color="var(--harmon-blue)"/>
          <stop offset="1" stop-color="var(--harmon-blue-deep)"/>
        </linearGradient>
      </defs>
      <polygon class="stripe-gray" points="30,0 200,0 500,560 330,560" fill="var(--stripe-gray)"/>
      <polygon class="stripe-charcoal" points="0,120 20,120 300,560 190,560 0,270" fill="var(--band-charcoal)"/>
      <polygon class="blue-band" points="60,165 1120,165 1120,455 240,455" fill="url(#blueBand)"/>
      <polygon class="blue-corner" points="0,300 160,560 0,560" fill="var(--harmon-blue-deep)"/>
      <polygon class="stripe-white" points="0,200 30,200 220,560 120,560 0,330" fill="var(--sign-white)"/>
      <polygon class="accent-stripe" points="1000,0 1030,0 1130,160 1100,160" fill="var(--harmon-blue)"/>
      <polygon class="footer-charcoal" points="0,470 430,470 470,560 0,560" fill="var(--band-charcoal)"/>
      <polygon class="footer-gray" points="430,470 520,470 560,560 470,560" fill="var(--band-gray)"/>
    </svg>

    <div class="brand">
      <span class="brand-name">Harmon</span>
      <span class="brand-sub">&amp; Company, Inc.</span>
    </div>
    <div class="brand-divider"></div>
    <div class="trade">
      <span class="first">General</span>
      <span>Contractors</span>
    </div>

    <h1 class="headline">We Build Client<br>Satisfaction</h1>

    <div class="details">
      <span class="license">CGC1234567</span>
      <div class="social" aria-label="Social media">
        <span class="social-square"></span>
        <span class="social-square"></span>
        <span class="social-square"></span>
      </div>
      <span class="location">Lakeview, Florida</span>
    </div>

    <div class="phone">407-555-0147</div>
    <div class="website">www.harmoncompany.net</div>
  </div>
</body>
</html>
```